Box Truck Wrap design with images and our logo

We need a design for the side of our box truck. We are an HVAC and Plumbing Company serving commercial and residential markets and want something catchy, not too busy but more than just logos. Maybe some equipment and/or verbiage of what we do. Real images would be a bonus. We want people to recognize our brand, see our story on the side of this tuck, much like a billboard, and be motivated to contact us for service.

Target Market(s)

Residential homeowners who need HVAC and Plumbing Services

Industry/Entity Type

Commercial and Residential HVAC

Font styles to use
Other font styles liked:
• Calibri

Colors
0054AA
0677BA
7BADD7
CADEEF
E8F1F8

Requirements
Must have
• Our logo, visible interpretation of what we do - Here is our website - www.quillfordpipeworks.example
Nice to have
• Integrated, easy design
Should not have
• Must not be too busy

```html
<!DOCTYPE html>
<html lang="en">
<head>
<meta charset="utf-8">
<title>Quillford Plumbing Heating &amp; Air Conditioning — Box Truck Wrap</title>
<link href="https://fonts.googleapis.com/css2?family=Montserrat:wght@600;700;800&family=Roboto+Condensed:wght@700&display=swap" rel="stylesheet">
<style>
  :root {
    --brand-blue: #2a4fa6;
    --band-blue: #2c4fa3;
    --panel-black: #121212;
    --panel-dark: #2a2a2a;
    --swoosh-light: #d9dde3;
    --text-white: #ffffff;
    --page-bg: #ffffff;
  }
  html, body {
    margin: 0;
    padding: 0;
    width: 1200px;
    height: 1200px;
    overflow: hidden;
    background: var(--page-bg);
  }
  .canvas {
    position: relative;
    width: 1200px;
    height: 1200px;
  }
  .wrap-art {
    position: absolute;
    left: 0;
    top: 0;
  }
  .brand-name {
    position: absolute;
    left: 92px;
    top: 450px;
    margin: 0;
    font-family: "Montserrat", sans-serif;
    font-weight: 800;
    font-size: 104px;
    letter-spacing: -1px;
    color: var(--brand-blue);
    line-height: 1;
  }
  .brand-trade {
    position: absolute;
    left: 300px;
    top: 580px;
    width: 420px;
    text-align: right;
    margin: 0;
    font-family: "Montserrat", sans-serif;
    font-weight: 700;
    font-size: 30px;
    line-height: 1.22;
    color: var(--text-white);
  }
  .service-list {
    position: absolute;
    left: 45px;
    top: 716px;
    width: 725px;
    height: 50px;
    margin: 0;
    padding: 0;
    list-style: none;
    display: flex;
    flex-wrap: wrap;
    justify-content: center;
    align-content: center;
    row-gap: 4px;
    font-family: "Roboto Condensed", sans-serif;
    font-weight: 700;
    font-size: 13px;
    letter-spacing: 0.4px;
    color: var(--text-white);
    text-transform: uppercase;
  }
  .service-list li + li::before {
    content: "•";
    margin: 0 6px;
    opacity: 0.7;
  }
  .service-list .line-break {
    flex-basis: 100%;
    height: 0;
  }
  .service-list .line-break + li::before { content: none; }
  .social-row {
    position: absolute;
    left: 84px;
    top: 790px;
    display: flex;
    gap: 10px;
  }
  .social-dot {
    width: 24px;
    height: 24px;
    border-radius: 50%;
    background: var(--text-white);
  }
  .cab-contact {
    position: absolute;
    left: 838px;
    top: 700px;
    margin: 0;
    font-family: "Montserrat", sans-serif;
    color: var(--text-white);
  }
  .cab-contact .phone {
    display: block;
    font-weight: 700;
    font-size: 22px;
    letter-spacing: 0.5px;
  }
  .cab-contact .web {
    display: block;
    margin-top: 2px;
    font-weight: 600;
    font-size: 12px;
  }
</style>
</head>
<body>
<main class="canvas">
  <svg class="wrap-art" width="1200" height="1200" viewBox="0 0 1200 1200" aria-hidden="false">
    <defs>
      <linearGradient id="equipmentTone" x1="0" y1="0" x2="1" y2="0">
        <stop offset="0" stop-color="#161616"/>
        <stop offset="0.45" stop-color="#2c2c2c"/>
        <stop offset="0.7" stop-color="#1c1c1c"/>
        <stop offset="1" stop-color="#111111"/>
      </linearGradient>
    </defs>
    <!-- cab side in brand blue -->
    <path class="cab-panel" d="M40 345 H1080 Q1160 345 1160 425 V855 H40 Z" fill="var(--band-blue)"/>
    <!-- light swoosh stripe -->
    <path class="swoosh-stripe" d="M40 345 H722 Q830 560 700 855 H40 Z" fill="var(--swoosh-light)"/>
    <!-- dark box panel with equipment backdrop -->
    <path class="box-panel" role="img" aria-label="Dark photo of a water heater and pipework behind the brand name"
          d="M40 345 H699 Q800 560 675 855 H40 Z" fill="url(#equipmentTone)"/>
    <!-- services band -->
    <rect class="service-band" x="45" y="716" width="725" height="50" fill="var(--band-blue)"/>
  </svg>

  <h1 class="brand-name">Quillford</h1>
  <p class="brand-trade">PLUMBING HEATING<br>&amp; AIR CONDITIONING</p>

  <ul class="service-list">
    <li>Residential Air Conditioning</li>
    <li>Residential Heating</li>
    <li>Indoor Air Quality</li>
    <li>Residential Plumbing</li>
    <li class="line-break" aria-hidden="true"></li>
    <li>Commercial Air Conditioning</li>
    <li>Commercial Heating</li>
    <li>Commercial Plumbing</li>
    <li>Garage Heaters</li>
  </ul>

  <div class="social-row" aria-label="Social media">
    <span class="social-dot"></span>
    <span class="social-dot"></span>
    <span class="social-dot"></span>
    <span class="social-dot"></span>
  </div>

  <p class="cab-contact">
    <span class="phone">(555) 014-2237</span>
    <span class="web">www.quillfordpipeworks.example</span>
  </p>
</main>
</body>
</html>
```